Scorvella Page Design

Hi, I am looking for someone who would help us make killer web page designs. There are 3 main pages that need to be designed:
1. Homepage-- Take a look at current design being worked on:
http://dev.scorvella-example.com/newsite/consumer.php#firstPage/1
2. Listing Page-- This is the current one being worked on: http://dev.scorvella-example.com/newsite/listing.php
The old one: http://www.scorvella-example.com/dentist
3. Profile Page:
The old design: http://www.scorvella-example.com/dentist/dentistprofile/Dr-Milo-Tandry-DDS-Escondido-CA/92025/id/10009
We are looking for someone who can take these designs to the next level and also provide an intuitive user interphase to help consumers and professionals navigate through the site appropriately and efficiently.
Our goal is to help guide users to help understand their values while educating them on the proper values that they need to look for. Creating trust and credibility is of most importance.
All designs must be mobile/desktop/tablet compatible
Target Market(s)
Professionals and Consumers, ages 25-55
Coding
Coded - Design and coding required
Number of Pages Required
5+ page
Look and feel

```html
<!DOCTYPE html>
<html lang="en">
<head>
<meta charset="utf-8">
<title>Scorvella – Rank, compare, select</title>
<link rel="stylesheet" href="https://fonts.googleapis.com/css2?family=Ubuntu:wght@400;500;700&display=swap">
<style>
:root{
  --green:#4cb748;
  --green-dark:#2f8f2c;
  --green-text:#48b23f;
  --navy:#29339a;
  --navy-deep:#232c8c;
  --ink:#333333;
  --muted:#555555;
  --soft:#f4f4f4;
  --white:#ffffff;
}
*{box-sizing:border-box;margin:0;padding:0}
html,body{width:1200px;height:3495px;overflow:hidden}
body{font-family:"Ubuntu",Arial,sans-serif;color:var(--ink);background:var(--white);position:relative}
a{color:inherit;text-decoration:none}

/* header */
.site-header{position:absolute;left:0;top:0;width:1200px;height:93px;background:var(--white)}
.brand{position:absolute;left:128px;top:28px;display:flex;align-items:center;gap:10px;font-size:30px;font-weight:400;color:#222}
.brand-dot{width:14px;height:14px;background:#222;border-radius:50%}
.main-nav{position:absolute;top:34px;left:405px;display:flex;gap:0;font-size:17px}
.main-nav a{display:block;padding:0 0}
.main-nav .home{position:absolute;left:0;color:var(--navy);width:60px}
.main-nav .about{position:absolute;left:85px;width:90px}
.main-nav .rank{position:absolute;left:195px;width:90px}
.main-nav .contact{position:absolute;left:305px;width:110px}
.search{position:absolute;left:822px;top:28px;width:245px;height:35px;border:1px solid #ccc;display:flex}
.search span{flex:1;font-size:12px;color:#aaa;padding:10px 8px}
.search button{width:34px;height:33px;border:0;background:var(--green);display:flex;align-items:center;justify-content:center}
.adv-search{position:absolute;left:982px;top:70px;font-size:11px;color:#888;text-decoration:underline}

/* hero */
.hero{position:absolute;left:0;top:93px;width:1200px;height:466px;background:linear-gradient(180deg,#d8d8d8 0%,#bdbdbd 55%,#9e9e9e 100%)}
.hero-tagline{position:absolute;top:48px;width:100%;text-align:center;font-size:25px;color:#222}
.hero-card{position:absolute;top:126px;width:270px;height:270px;border-radius:50%;border:5px solid var(--white);box-shadow:0 4px 14px rgba(0,0,0,.25)}
.hero-card.pro{left:222px;background:radial-gradient(circle at 50% 40%,#ffffff,#e2e6ea 70%,#c5ccd3)}
.hero-card.consumer{left:629px;background:radial-gradient(circle at 50% 40%,#ffffff,#ececec 70%,#cfcfcf)}
.hero-btn{position:absolute;top:310px;height:40px;display:flex;align-items:center;justify-content:center;font-size:15px;font-weight:500;color:var(--white)}
.hero-btn.pro{left:280px;width:156px;background:var(--navy)}
.hero-btn.consumer{left:680px;width:159px;background:var(--green)}
.hero-dots{position:absolute;top:430px;left:566px;display:flex;gap:9px}
.hero-dots i{width:9px;height:9px;border-radius:50%;background:#e8e8e8}
.hero-dots i:first-child{background:#fff}

/* ribbon heading */
.ribbon{position:absolute;left:408px;width:384px;height:75px}
.ribbon svg{position:absolute;left:0;top:0}
.ribbon h2{position:absolute;left:0;top:0;width:100%;height:60px;display:flex;align-items:center;justify-content:center;font-size:30px;font-weight:500;color:var(--white)}

/* about */
.about{position:absolute;left:0;top:559px;width:1200px;height:457px;background:var(--navy)}
.about-photo{position:absolute;left:130px;top:175px;width:455px;height:240px;background:linear-gradient(135deg,#3c4650,#8a949e 55%,#d7dde2)}
.features{position:absolute;left:610px;top:180px;width:460px;color:var(--white)}
.features h3{font-size:16px;font-weight:700;margin-bottom:16px}
.features p{font-size:13px;line-height:24px}
.enter-btn{position:absolute;left:610px;top:357px;width:187px;height:42px;background:var(--green);color:var(--white);font-size:12px;font-weight:700;display:flex;align-items:center;justify-content:center}
.about-pointer{position:absolute;left:578px;top:1016px}

/* power */
.power{position:absolute;left:0;top:1016px;width:1200px;height:424px;background:var(--white)}
.power-headline{position:absolute;left:154px;top:98px;width:480px;font-size:28px;line-height:33px;font-weight:700;color:var(--green-text)}
.power-divider{position:absolute;left:645px;top:86px;width:1px;height:191px;background:#bbb}
.power-list{position:absolute;left:666px;top:98px;list-style:none;font-size:13px;font-weight:700;line-height:24px;color:#222}
.power-copy{position:absolute;left:150px;top:300px;width:900px;text-align:center;font-size:13px;line-height:25px;color:#333}

/* rankings */
.rankings{position:absolute;left:0;top:1440px;width:1200px;height:941px;background:var(--soft)}
.rank-card{position:absolute;width:294px}
.rank-photo{width:294px;height:183px}
.rank-card h3{font-size:16px;font-weight:700;color:#333;margin-top:22px}
.rank-card p{font-size:12px;line-height:23px;color:#555;margin-top:8px}
.read-more{display:inline-block;margin-top:10px;width:82px;height:22px;background:var(--navy);color:var(--white);font-size:11px;font-weight:700;text-align:center;line-height:22px}

/* contact */
.contact{position:absolute;left:0;top:2381px;width:1200px;height:834px;background:linear-gradient(100deg,#3a3f44 0%,#565c61 35%,#4a4f53 65%,#2e3236 100%)}
.field{position:absolute;left:363px;width:471px;border:1px solid #e6e6e6;color:var(--white);font-size:14px;padding:20px 16px}
.send-btn{position:absolute;left:363px;top:655px;width:471px;height:63px;background:var(--green);color:var(--white);font-size:22px;font-weight:700;display:flex;align-items:center;justify-content:center}

/* footer */
.site-footer{position:absolute;left:0;top:3215px;width:1200px;height:280px;background:var(--navy)}
.footer-col{position:absolute;top:36px;color:var(--white)}
.footer-col h4{font-size:17px;font-weight:500;margin-bottom:28px}
.footer-col ul{list-style:none;font-size:14px;line-height:30.5px}
.social{display:flex;gap:12px;margin-top:4px}
.social i{width:18px;height:18px;border-radius:50%;background:var(--white)}
.copyright{position:absolute;top:230px;width:100%;text-align:center;font-size:13px;color:var(--white)}
</style>
</head>
<body>

<header class="site-header">
  <div class="brand"><span class="brand-dot"></span>Scorvella</div>
  <nav class="main-nav">
    <a class="home" href="#">Home</a>
    <a class="about" href="#">About Us</a>
    <a class="rank" href="#">Rankings</a>
    <a class="contact" href="#">Contact Us</a>
  </nav>
  <div class="search"><span>Search</span>
    <button aria-label="Search"><svg width="14" height="14" viewBox="0 0 14 14"><circle cx="5.5" cy="5.5" r="4" fill="none" stroke="#fff" stroke-width="2"/><line x1="8.5" y1="8.5" x2="13" y2="13" stroke="#fff" stroke-width="2"/></svg></button>
  </div>
  <a class="adv-search" href="#">Advanced Search</a>
</header>

<section class="hero" role="img" aria-label="Blurred office background">
  <p class="hero-tagline">Rank, compare, select- the professional way</p>
  <div class="hero-card pro" role="img" aria-label="Photo of a doctor in a white coat with a stethoscope"></div>
  <div class="hero-card consumer" role="img" aria-label="Photo of a smiling consumer in a white blouse"></div>
  <a class="hero-btn pro" href="#">For Professional</a>
  <a class="hero-btn consumer" href="#">Consumer</a>
  <div class="hero-dots"><i></i><i></i><i></i><i></i></div>
</section>

<section class="about">
  <div class="ribbon" style="top:58px">
    <svg width="384" height="75" viewBox="0 0 384 75"><polygon points="0,15 60,15 60,75 0,75 22,45" fill="var(--green-dark)"/><polygon points="384,15 324,15 324,75 384,75 362,45" fill="var(--green-dark)"/><rect x="40" y="0" width="304" height="63" fill="var(--green)"/></svg>
    <h2>About Us</h2>
  </div>
  <div class="about-photo" role="img" aria-label="Photo of hands holding a tablet showing charts"></div>
  <div class="features">
    <h3>Features</h3>
    <p>Until now it's been impossible to find, compare and select high-quality professionals based on your personal needs and values without someone else's marketing agenda getting in the way. Typical review sites tell you someone else's experienced (perceived value) but say nothing about quality of the products and services they received.</p>
  </div>
  <a class="enter-btn" href="#">ENTER SCORVELLA !</a>
</section>
<svg class="about-pointer" width="46" height="33" viewBox="0 0 46 33" style="position:absolute;z-index:2"><polygon points="0,0 46,0 23,33" fill="var(--navy)"/></svg>

<section class="power">
  <p class="power-headline">Scorvella gives you this power! You control what's important and find professionals ranked based by what's important to YOU.</p>
  <div class="power-divider"></div>
  <ul class="power-list">
    <li>Price?</li>
    <li>Actual work examples?</li>
    <li>Location?</li>
    <li>Quality Ranking?</li>
    <li>Years in practice?</li>
    <li>"Hospitality" consumer ratings?</li>
    <li>Industry professional recommendation?</li>
  </ul>
  <p class="power-copy">Cut through the clutter, eliminate the guessing game and display what is most important to you in selecting professional. Compare apples to apples by ranking objectively and accurately.Scorvella give you the power to be a smart shopper to compare and select more specifically and precisely than ever before. Professionals now can reach consumer who share the values of what they do best.</p>
</section>

<section class="rankings">
  <div class="ribbon" style="top:58px">
    <svg width="384" height="75" viewBox="0 0 384 75"><polygon points="0,15 60,15 60,75 0,75 22,45" fill="var(--green-dark)"/><polygon points="384,15 324,15 324,75 384,75 362,45" fill="var(--green-dark)"/><rect x="40" y="0" width="304" height="63" fill="var(--green)"/></svg>
    <h2>Rankings</h2>
  </div>

  <article class="rank-card" style="left:130px;top:177px">
    <div class="rank-photo" role="img" aria-label="Photo of healthcare staff reviewing a clipboard" style="background:linear-gradient(135deg,#7fa7c4,#dfe8ee)"></div>
    <h3>Healthcare</h3><p>Lorem Ipsum is simply dummy text of the printing and typesetting industry.</p><a class="read-more" href="#">Read More</a>
  </article>
  <article class="rank-card" style="left:454px;top:177px">
    <div class="rank-photo" role="img" aria-label="Photo of a judge's gavel on a desk" style="background:linear-gradient(135deg,#5a3a22,#c59a6c)"></div>
    <h3>Legal</h3><p>Lorem Ipsum is simply dummy text of the printing and typesetting industry.</p><a class="read-more" href="#">Read More</a>
  </article>
  <article class="rank-card" style="left:776px;top:177px">
    <div class="rank-photo" role="img" aria-label="Photo of hands giving a massage" style="background:linear-gradient(135deg,#6f8fae,#d8c3b4)"></div>
    <h3>Personal Care</h3><p>Lorem Ipsum is simply dummy text of the printing and typesetting industry.</p><a class="read-more" href="#">Read More</a>
  </article>

  <article class="rank-card" style="left:130px;top:550px">
    <div class="rank-photo" role="img" aria-label="Photo of a nurse greeting an elderly patient outdoors" style="background:linear-gradient(135deg,#6d9b5a,#d5e2c6)"></div>
    <h3>Home Care</h3><p>Lorem Ipsum is simply dummy text of the printing and typesetting industry.</p><a class="read-more" href="#">Read More</a>
  </article>
  <article class="rank-card" style="left:454px;top:550px">
    <div class="rank-photo" role="img" aria-label="Photo of a waiter serving plated dishes" style="background:linear-gradient(135deg,#3b2a22,#b48a6c)"></div>
    <h3>Food &amp; Beverage</h3><p>Lorem Ipsum is simply dummy text of the printing and typesetting industry.</p><a class="read-more" href="#">Read More</a>
  </article>
  <article class="rank-card" style="left:776px;top:550px">
    <div class="rank-photo" role="img" aria-label="Photo of a car assembly line" style="background:linear-gradient(135deg,#8a97a3,#e1e6ea)"></div>
    <h3>Automotive</h3><p>Lorem Ipsum is simply dummy text of the printing and typesetting industry.</p><a class="read-more" href="#">Read More</a>
  </article>
</section>

<section class="contact" role="img" aria-label="Dimmed photo of a doctor in a clinic">
  <div class="ribbon" style="top:56px">
    <svg width="384" height="75" viewBox="0 0 384 75"><polygon points="0,15 60,15 60,75 0,75 22,45" fill="var(--green-dark)"/><polygon points="384,15 324,15 324,75 384,75 362,45" fill="var(--green-dark)"/><rect x="40" y="0" width="304" height="63" fill="var(--green)"/></svg>
    <h2>Contact Us</h2>
  </div>
  <div class="field" style="top:173px;height:63px">Type Of Inquiry</div>
  <div class="field" style="top:259px;height:65px">Name</div>
  <div class="field" style="top:357px;height:65px">E-Mail</div>
  <div class="field" style="top:455px;height:177px">Message</div>
  <a class="send-btn" href="#">SEND</a>
</section>

<footer class="site-footer">
  <div class="footer-col" style="left:170px">
    <h4>Company</h4>
    <ul><li>Home</li><li>About</li><li>FAQ</li></ul>
  </div>
  <div class="footer-col" style="left:350px">
    <h4>&nbsp;</h4>
    <ul><li>Register</li><li>Terms of Use</li><li>Privacy Policy</li></ul>
  </div>
  <div class="footer-col" style="left:533px">
    <h4>Services</h4>
    <ul><li>Find A Dental Lab</li><li>Find A Dentist</li><li>Find A Plastic Surgeon</li></ul>
  </div>
  <div class="footer-col" style="left:776px">
    <h4>Connect With Us</h4>
    <div class="social"><i></i><i></i><i></i><i></i><i></i><i></i></div>
  </div>
  <p class="copyright">© 2015 Company Name,All Rights Reserved</p>
</footer>

</body>
</html>
```